An anniversary gift for my girlfriend

My girlfriend and I have been dating for almost 2 years. We met online and this has afforded us the really unique opportunity to have the first words we said to each other (the whole conversation, in fact) preserved. We're moving in together in a few months and she doesn't know that I saved the conversation. I've been waiting for this to turn it into something we can hang in our new place.

The only phrase I want to use is:
"Well if you dislike people's knees then I think we'll get along famously"

It's an Nobody Leaves Before Midnight in Portland reference for the curious.

I want the poster to use the words themselves as the art; I'm thinking typography. I'd like it to match her aesthetic, she likes to wear Nora Vell and T. Brisk. Colors shouldn't be anything too "girly". Somewhere I'd like to include the date June 1, 2015. It shouldn't be a major piece of the poster though, just a way to denote the date.

It should fit (and be fully visible in) a 16x20 (inches) frame

Thanks in advance for the work!

Requirements
Must have
• Must use only the words: "Well if you dislike people's knees then I think we'll get along famously"
• I want this to be typography, so making the phrase the center of the poster and the art itself.

```html
<!DOCTYPE html>
<html lang="en">
<head>
<meta charset="utf-8">
<title>Well If You Dislike People's Knees</title>
<link href="https://fonts.googleapis.com/css2?family=Bebas+Neue&family=Righteous&display=swap" rel="stylesheet">
<style>
  :root {
    --warm-top: #f3865c;
    --warm-mid: #c9725e;
    --dusk: #8a6570;
    --deep-blue: #2c5f8c;
    --night-blue: #1e4a74;
    --glow: rgba(255, 236, 190, 0.85);
    --cream: #fdf1de;
    --frame-wash: rgba(255, 255, 255, 0.18);
    --date-blue: #4f98dc;
  }
  html, body {
    margin: 0;
    padding: 0;
    width: 960px;
    height: 1200px;
    overflow: hidden;
    background: #1b2a3a;
  }
  .poster {
    position: relative;
    width: 960px;
    height: 1200px;
    overflow: hidden;
  }
  .poster__backdrop {
    position: absolute;
    inset: 0;
    background:
      radial-gradient(ellipse 340px 160px at 470px 0px, var(--glow), transparent 75%),
      radial-gradient(ellipse 520px 380px at 700px 620px, rgba(255, 200, 140, 0.35), transparent 70%),
      radial-gradient(ellipse 420px 300px at 120px 800px, rgba(90, 130, 180, 0.45), transparent 70%),
      linear-gradient(180deg, var(--warm-top) 0%, var(--warm-mid) 28%, var(--dusk) 55%, var(--deep-blue) 82%, var(--night-blue) 100%);
  }
  .poster__frame {
    position: absolute;
    inset: 0;
    border: 24px solid var(--frame-wash);
    box-sizing: border-box;
  }
  .quote {
    position: absolute;
    left: 0;
    top: 0;
    width: 984px;
    margin: 0;
    text-align: center;
    color: var(--cream);
    font-weight: 400;
  }
  .quote__line {
    position: absolute;
    left: 0;
    width: 100%;
    display: block;
    line-height: 1;
    white-space: nowrap;
  }
  .quote__line--solid {
    font-family: "Bebas Neue", "Arial Narrow", sans-serif;
    font-size: 122px;
    letter-spacing: 1px;
  }
  .quote__line--outline {
    font-family: "Righteous", "Arial", sans-serif;
    font-size: 104px;
    color: transparent;
    -webkit-text-stroke: 3px var(--cream);
    letter-spacing: 2px;
  }
  .date {
    position: absolute;
    left: 0;
    width: 960px;
    top: 1146px;
    text-align: center;
    font-family: "Bebas Neue", "Arial Narrow", sans-serif;
    font-size: 20px;
    letter-spacing: 1px;
    color: var(--date-blue);
    margin: 0;
  }
</style>
</head>
<body>
<main class="poster">
  <div class="poster__backdrop" role="img" aria-label="Soft bokeh of warm orange light fading into deep blue"></div>
  <div class="poster__frame"></div>
  <h1 class="quote">
    <span class="quote__line quote__line--solid" style="top:168px">"Well if you</span>
    <span class="quote__line quote__line--solid" style="top:270px">dislike</span>
    <span class="quote__line quote__line--solid" style="top:372px">people's knees,</span>
    <span class="quote__line quote__line--solid" style="top:474px">then I think</span>
    <span class="quote__line quote__line--outline" style="top:582px; left:-90px">we'll</span>
    <span class="quote__line quote__line--outline" style="top:684px">get along</span>
    <span class="quote__line quote__line--solid" style="top:788px">famously"</span>
  </h1>
  <p class="date">June 1, 2015</p>
</main>
</body>
</html>
```